Flyer-Design für Dienstleistungen im vorbeugenden Brandschutz und der Ersten Hilfe
Zielgruppe
Wachturm Brandschutz & Erste-Hilfe
Meine Firma spezialisiert sich auf Dienstleistungen im vorbeugenden Brandschutz und im Bereich der Ersten Hilfe.
Mit meiner Firma biete ich folgende Dienstleistungen und Produkte an:
Diensteistungen:
- jährliche Brandschutzunterweisung
- Brandschutzhelferausbildungen nach DGUV Information 205-023
- Brandsicherheitswachen für Unternehmen und Veranstaltungen
- Sanitätsdienste für Unternehmen und Veranstaltungen
- externer Brandschutzbeauftragter
- Vertrieb und Wartung von Feuerlöschern / Brandschutzbedarf
- betriebliche Erste-Hilfe Schulungen / Erste Hilfe Kurs für den Führerschein
- Wartung und Vertrieb von Erste-Hilfe-Material / Ausstattung
- Wartung, Vertrieb und Schulungen von Automatisierten Externen Defibrillatoren
Zu den folgenden Dienstleistungen sollte die Möglichkeit bestehen, detaillierte Texte einzusetzen. Die Themengebite können auch zusammengefasst werden:
Themengebiet 1 (Brandschutz)
Themengebiet 2 (Erste-Hilfe)
Meine Zielgruppe sind primär Firmen, allerdings biete ich die Dienstleistungen auch an Privatpersonen an.
Aufgabenstellung
Die Schriftart in meinem Logo ist 'Avenir'.
Die Firmenfarben orange und grau sollten berücksichtigt werden.
Das Format sollte DIN A4 doppelseitig bedruckt und in 3 Teile gefaltet sein (Ergebnis DIN Lang)
Auf der letzten Seite sollten die Kontaktdaten stehen, sowie mindestens das Logo (Mitglied im BKSV (Bund Kommunaler Sicherheits-Vereine))

```html
<!DOCTYPE html>
<html lang="de">
<head>
<meta charset="utf-8">
<title>Dienstleistungen – Brandschutz &amp; Erste-Hilfe</title>
<link href="https://fonts.googleapis.com/css2?family=Nunito+Sans:wght@300;400&display=swap" rel="stylesheet">
<style>
  :root {
    --orange: #e8661c;
    --panel: #e1e1e1;
    --text: #6a6a6a;
    --fold: #dcdcdc;
    --paper: #ffffff;
  }
  html, body {
    margin: 0;
    padding: 0;
    width: 1200px;
    height: 849px;
    overflow: hidden;
    background: var(--paper);
  }
  .flyer {
    position: relative;
    width: 1200px;
    height: 849px;
    font-family: "Nunito Sans", "Avenir", sans-serif;
    font-weight: 300;
    color: var(--text);
  }
  .fold {
    position: absolute;
    top: 0;
    width: 1px;
    height: 849px;
    background: var(--fold);
    z-index: 2;
  }
  .fold--first { left: 414px; }
  .fold--second { left: 788px; }

  .title-band {
    position: absolute;
    left: 24px; top: 22px;
    width: 764px; height: 119px;
    background: var(--orange);
  }
  .title-band h1 {
    margin: 0;
    position: absolute;
    left: 211px; top: 24px;
    font-weight: 300;
    font-size: 57px;
    line-height: 1;
    color: #fff;
    letter-spacing: -0.3px;
  }
  .photo {
    position: absolute;
    left: 24px; top: 169px;
    width: 764px; height: 381px;
    background:
      radial-gradient(ellipse at 55% 75%, #d9505a 0%, rgba(217,80,90,0) 45%),
      radial-gradient(ellipse at 20% 80%, #c9404b 0%, rgba(201,64,75,0) 40%),
      radial-gradient(ellipse at 85% 30%, #b8444c 0%, rgba(184,68,76,0) 45%),
      linear-gradient(160deg, #9e3a40 0%, #c8454f 45%, #d95b63 70%, #b03a44 100%);
  }

  .panel {
    position: absolute;
    background: var(--panel);
    box-sizing: border-box;
  }
  .panel--overview { left: 815px; top: 22px; width: 364px; height: 524px; padding: 16px 14px 0 14px; }
  .panel--fire { left: 24px; top: 641px; width: 363px; height: 187px; padding: 26px 14px 0 14px; }
  .panel--aid { left: 424px; top: 641px; width: 364px; height: 187px; padding: 26px 14px 0 14px; }
  .panel--duty { left: 815px; top: 641px; width: 364px; height: 187px; padding: 26px 14px 0 14px; }

  .service-list {
    list-style: none;
    margin: 0;
    padding: 0;
    font-size: 16px;
    line-height: 20px;
    letter-spacing: 0.1px;
    hyphens: manual;
  }
  .service-list li {
    position: relative;
    padding-left: 17px;
    margin-bottom: 8px;
  }
  .service-list li::before {
    content: "»";
    position: absolute;
    left: 0;
    top: 0;
    font-size: 12px;
  }
  .panel--overview .service-list li { margin-bottom: 8px; }

  .topic-band {
    position: absolute;
    left: 24px; top: 569px;
    width: 1154px; height: 56px;
    background: var(--orange);
  }
  .topic {
    position: absolute;
    top: 0;
    margin: 0;
    height: 56px;
    line-height: 56px;
    font-weight: 400;
    font-size: 34px;
    color: #fff;
    text-align: center;
    transform: translateX(-50%);
    white-space: nowrap;
  }
  .topic--fire { left: 183px; }
  .topic--aid { left: 577px; }
  .topic--duty { left: 972px; }
</style>
</head>
<body>
<main class="flyer">
  <div class="fold fold--first"></div>
  <div class="fold fold--second"></div>

  <header class="title-band">
    <h1>Dienstleistungen</h1>
  </header>

  <div class="photo" role="img" aria-label="Foto: Nahaufnahme vieler roter Feuerlöscher mit Griffen und Schläuchen"></div>

  <section class="panel panel--overview">
    <ul class="service-list">
      <li>jährliche Brandschutzunterweisung</li>
      <li>Brandschutzhelferausbildungen nach DGUV Information 205-023</li>
      <li>Brandsicherheitswachen für Unternehmen und Veranstaltungen</li>
      <li>Sanitätsdienste für Unternehmen und Ver­anstaltungen</li>
      <li>externer Brandschutzbeauftragter</li>
      <li>Vertrieb und Wartung von Feuerlöschern / Brandschutzbedarf</li>
      <li>betriebliche Erste-Hilfe Schulungen / Ers­te Hilfe Kurs für den Führerschein</li>
      <li>Wartung und Vertrieb von Erste-Hilfe-Ma­terial / Ausstattung</li>
      <li>Wartung, Vertrieb und Schulungen von Automatisierten Externen Defibrillatoren</li>
    </ul>
  </section>

  <div class="topic-band">
    <h2 class="topic topic--fire">Brandschutz</h2>
    <h2 class="topic topic--aid">Erste-Hilfe</h2>
    <h2 class="topic topic--duty">Dienste</h2>
  </div>

  <section class="panel panel--fire">
    <ul class="service-list">
      <li>jährliche Brandschutzunterweisung</li>
      <li>Brandschutzhelferausbildungen nach DGUV Information 205-023</li>
      <li>Vertrieb und Wartung von Feuerlöschern / Brandschutzbedarf</li>
    </ul>
  </section>

  <section class="panel panel--aid">
    <ul class="service-list">
      <li>betriebliche Erste-Hilfe Schulungen / Ers­te Hilfe Kurs für den Führerschein</li>
      <li>Wartung und Vertrieb von Erste-Hilfe-Ma­terial / Ausstattung</li>
      <li>Wartung, Vertrieb und Schulungen von Automatisierten Externen Defibrillatoren</li>
    </ul>
  </section>

  <section class="panel panel--duty">
    <ul class="service-list">
      <li>Brandsicherheitswachen für Unternehmen und Veranstaltungen</li>
      <li>Sanitätsdienste für Unternehmen und Ver­anstaltungen</li>
    </ul>
  </section>
</main>
</body>
</html>
```